New Wordpress Design Project - Australian native plant nursery

I'm Seeking a wordpress website with landing page with contact details and social links, that page will link to another 4 pages. I'm happy to just add in the information once the template is set up (draft text provided on word doc).
Needing pages of information pages for:
- Nursery, what we carry and that we provide garden design services, pictures of plants and gardens
- Native flowers & what we provide, flower arrangements for weddings, special occasions, pictures
- Giftwear short blurb that we carry local artisan giftwear, pictures
- about us with history of the nursery & pictures
* Also wanting a link for e-gift cards. The link will go to an external page (square) so I don’t need to set up the website for purchases.
Social media links
Social links
https://www.facebook.com/TheBrambleHollow
https://www.instagram.com/thebramblehollownursery

Two local native nursery websites that I like the style of:
https://www.harbourfernplantnursery.com.au/
https://www.belmaro.com.au/

I'm using two versions of our logo, we have the smaller circle and then the other logo which is stretched out. We have used the second design for our signs at the nursery, I've asked the sign guy for a copy of the design as I don't currently have one. I have vector files of the other design.

We have wordpress set up with elemantor and hosting with godaddy, I can send you the logon details once design is confirmed.

Target Market(s)

Anyone who likes gardening, we have a pretty even spread of customers across male/female and all ages

Industry/Entity Type

Garden centre with native plants, flowers and giftwear

Coding

Coded - Design and coding required

Colors
0054AA
0677BA
7BADD7
CADEEF
E8F1F8
0094D4
00A9DD
6FCCEA
C7EBF8
E9F6FB
00AB8E
00BBA5
67D7C9
C6EFE9
E9F9F6

Requirements
Must have
• Organic/modern/minimalist design
Nice to have
• Blue/white/green, flannel flowers as per logo

```html
<!DOCTYPE html>
<html lang="en">
<head>
<meta charset="utf-8">
<title>The Bramble Hollow – Australian Plants, Flowers and Giftware</title>
<link rel="stylesheet" href="https://fonts.googleapis.com/css2?family=Playfair+Display:wght@400;600;700&family=Arimo:wght@400;700&display=swap">
<style>
:root{
  --blue-deep:#24597a;
  --blue-head:#2d6482;
  --teal:#0e7f6b;
  --footer:#0f7b63;
  --mint-band:#eaf3f1;
  --grey-band:#e1e8ec;
  --text:#3e4a52;
  --white:#ffffff;
}
*{margin:0;padding:0;box-sizing:border-box}
html,body{width:1200px;height:4815px;overflow:hidden}
body{position:relative;background:var(--white);font-family:"Arimo",Arial,sans-serif;color:var(--text);font-size:13.5px;line-height:1.36}
a{color:inherit;text-decoration:none}
.abs{position:absolute}
h1,h2,h3{font-family:"Playfair Display",Georgia,serif;font-weight:700}
.section-title{color:var(--blue-deep);font-size:56px;line-height:1}
.btn{display:inline-block;background:var(--teal);color:var(--white);font-family:"Playfair Display",Georgia,serif;font-weight:700;font-size:14px;letter-spacing:.3px;border-radius:28px;width:164px;height:52px;line-height:52px;text-align:center}

/* hero */
.hero{left:0;top:0;width:1200px;height:735px;background:linear-gradient(160deg,#6f94b6 0%,#567c6a 35%,#6e5a45 65%,#3c5430 100%)}
.hero-wave{left:0;top:560px;width:1200px;height:180px}
.header-bar{left:0;top:0;width:1200px;height:122px;background:rgba(36,89,122,.88)}
.brand-circle{left:118px;top:8px;width:158px;height:158px;border-radius:50%;background:var(--blue-head);border:2px solid rgba(255,255,255,.85);display:flex;align-items:center;justify-content:center;text-align:center;color:var(--white);font-family:"Playfair Display",Georgia,serif;font-size:21px;line-height:1.15}
.call{left:780px;top:22px;color:var(--white);font-family:"Playfair Display",Georgia,serif;font-weight:700;font-size:15px;display:flex;align-items:center;gap:6px}
.social-top{top:16px;width:34px;height:34px;border-radius:50%;border:2px solid var(--white)}
.nav{left:618px;top:70px;display:flex;gap:44px;color:var(--white);font-family:"Playfair Display",Georgia,serif;font-size:17px}
.hero-title{left:115px;top:280px;color:var(--white);font-size:63px;line-height:1.15}
.hero-sub{left:117px;top:430px;color:var(--white);font-family:"Playfair Display",Georgia,serif;font-size:20px}

/* native plants */
.np-photo{left:143px;top:840px;width:450px;height:450px;border-radius:50%;background:radial-gradient(circle at 40% 40%,#4f7a3a,#2f4f25 60%,#6b5d4a)}
.np-text{left:628px;top:866px;width:440px}
.np-text h2{margin-bottom:22px}
.np-text .lead{font-weight:700;font-size:14.5px;margin-bottom:16px;color:#333}
.np-text p{margin-bottom:16px}
.deco{background:radial-gradient(ellipse at center,rgba(190,200,205,.35),rgba(190,200,205,0) 70%)}

/* flowers */
.flowers-band{left:0;top:1290px;width:1200px;height:935px}
.flowers-head{left:0;top:1483px;width:1200px;text-align:center}
.flowers-intro{left:255px;top:1560px;width:690px;text-align:center}
.flower-card{top:1662px;width:295px}
.flower-card .photo{height:253px}
.flower-card p{margin-top:28px;text-align:center;padding:0 14px}

/* giftwear */
.gift-text{left:117px;top:2378px;width:470px}
.gift-text h2{margin-bottom:18px}
.gift-text p{margin-bottom:18px}
.gift-big{left:623px;top:2368px;width:337px;height:427px;background:linear-gradient(160deg,#c87c8e,#6f8a3c 45%,#d9b64b 70%,#4e6a3a)}
.gift-small{left:795px;top:2548px;width:272px;height:257px;border:8px solid var(--white);background:linear-gradient(150deg,#a88b93,#6b7a4b 55%,#8b6e74)}

/* history */
.history-band{left:0;top:2908px;width:1200px;height:482px;background:var(--grey-band)}
.history-head{left:0;top:2978px;width:1200px;text-align:center}
.history-intro{left:270px;top:3050px;width:660px;text-align:center}
.video{left:250px;top:3157px;width:698px;height:391px;background:linear-gradient(180deg,#5e8fc7 0%,#2f5f8f 22%,#9aa68e 45%,#4d5a3b 75%,#cfc7b8 100%)}
.play{left:561px;top:3314px;width:76px;height:76px;border-radius:50%;border:4px solid var(--white)}

/* nursery now */
.now-head{left:0;top:3595px;width:1200px;text-align:center}
.now-head h2{display:inline-block;color:var(--teal);font-size:54px;border-bottom:2px solid var(--teal);line-height:1.05;padding-bottom:2px}
.now-title{left:117px;top:3825px;width:300px;color:var(--blue-deep);font-size:42px;line-height:1.08}
.now-text{left:120px;top:4025px;width:375px;font-size:14.5px}
.now-text p{margin-bottom:22px}
.now-photo{left:572px;top:3696px;width:504px;height:504px;border-radius:50%;background:radial-gradient(circle at 60% 55%,#e6e8cf,#8da36a 40%,#2f4a24 80%)}

/* footer */
.footer-wave{left:0;top:4215px;width:1200px;height:600px}
.footer-brand{left:133px;top:4455px;width:170px;height:170px;border-radius:50%;border:2px solid var(--white);display:flex;align-items:center;justify-content:center;text-align:center;color:var(--white);font-family:"Playfair Display",Georgia,serif;font-size:22px;line-height:1.15}
.footer-col h3{color:var(--white);font-size:22px;margin-bottom:22px}
.footer-col{color:var(--white);font-size:13.5px}
.links li{list-style:none;margin-bottom:12px}
.contact-row{display:flex;align-items:flex-start;gap:14px;margin-bottom:18px}
.contact-ico{flex:0 0 40px;height:40px;border-radius:50%;border:2px solid var(--white);display:flex;align-items:center;justify-content:center}
.email{margin-top:18px;width:248px;height:44px;border-radius:24px;background:var(--white);color:#444;display:flex;align-items:center;justify-content:space-between;padding:0 2px 0 18px}
.email-go{width:40px;height:40px;border-radius:50%;background:var(--teal);display:flex;align-items:center;justify-content:center}
.social-foot{display:flex;gap:12px;margin-top:24px}
.social-foot a{width:36px;height:36px;border-radius:50%;background:var(--white);display:block}
.footer-rule{left:117px;top:4725px;width:966px;height:1px;background:rgba(255,255,255,.35)}
.copyright{left:0;top:4768px;width:1200px;text-align:center;color:var(--white);font-size:13px}
</style>
</head>
<body>

<div class="abs hero" role="img" aria-label="Photo of the nursery path lined with potted native plants beside the timber shed"></div>
<svg class="abs hero-wave" viewBox="0 0 1200 180" preserveAspectRatio="none" aria-hidden="true">
  <path d="M0 90 C250 210 520 200 760 150 C950 110 1080 110 1200 80 L1200 180 L0 180Z" fill="#fff"/>
</svg>
<header>
  <div class="abs header-bar"></div>
  <a class="abs brand-circle" href="#">The<br>Bramble<br>Hollow</a>
  <div class="abs call">
    <svg width="15" height="15" viewBox="0 0 24 24" aria-hidden="true"><path fill="#fff" d="M6.6 10.8a15 15 0 0 0 6.6 6.6l2.2-2.2c.3-.3.7-.4 1-.2 1.1.4 2.3.6 3.6.6.6 0 1 .4 1 1V20c0 .6-.4 1-1 1A17 17 0 0 1 3 4c0-.6.4-1 1-1h3.5c.6 0 1 .4 1 1 0 1.3.2 2.5.6 3.6.1.3 0 .7-.2 1z"/></svg>
    CALL US: 900 414 272
  </div>
  <a class="abs social-top" style="left:996px" href="#" aria-label="Social link one"></a>
  <a class="abs social-top" style="left:1040px" href="#" aria-label="Social link two"></a>
  <nav class="abs nav"><a href="#">Nursery</a><a href="#">Native flowers</a><a href="#">Giftwear</a><a href="#">About Us</a></nav>
</header>
<h1 class="abs hero-title">The Bramble<br>Hollow</h1>
<div class="abs hero-sub">Australian Plants * Flowers And Giftware</div>

<div class="abs np-photo" role="img" aria-label="Photo of potted native shrubs with price tags"></div>
<section class="abs np-text">
  <h2 class="section-title">Native plants</h2>
  <p class="lead">Welcome to our native plant nursery information page!</p>
  <p>At our nursery, we provide native plants that thrive in their local environment. Native plants are essential for preserving biodiversity, and they support pollinators and other wildlife while reducing human impact on the environment.</p>
  <p>At our nursery, we offer a wide selection of native plants that are suitable for a variety of different environments, and we provide planting and care instructions to ensure that your plants thrive once they're in the ground.</p>
  <a class="btn" href="#">READ MORE</a>
</section>

<svg class="abs flowers-band" viewBox="0 0 1200 935" preserveAspectRatio="none" aria-hidden="true">
  <path d="M0 40 C160 110 330 110 520 80 C760 40 980 30 1200 60 L1200 935 L0 935Z" fill="#eaf3f1"/>
</svg>
<div class="abs deco" style="left:890px;top:1260px;width:300px;height:250px" role="img" aria-label="Faint line drawing of flannel flowers"></div>
<div class="abs flowers-head"><h2 class="section-title">Flowers</h2></div>
<p class="abs flowers-intro">At the nursery, we specialize in creating unique arrangements using locally sourced native Australian flowers. Our team of experienced florists are passionate about showcasing the beauty of our country's flora and fauna through unique and beautiful bespoke floral designs.</p>
<div class="abs flower-card" style="left:117px">
  <div class="photo" style="background:linear-gradient(150deg,#4f7d3a,#e88a9c 50%,#3d6a2e)" role="img" aria-label="Photo of pink native flower"></div>
  <p>Our native flower arrangements are perfect for any occasion – from weddings and corporate events to simple gifts for loved ones. The vibrant colours and textures of our native flowers can add a touch of the Australian landscape to any space.</p>
</div>
<div class="abs flower-card" style="left:452px">
  <div class="photo" style="background:radial-gradient(circle at 45% 45%,#e07fc6,#a34d92 30%,#3f6630 60%)" role="img" aria-label="Photo of pink flower with raindrops"></div>
  <p>We believe that sustainability is important, and as such, all of our native flowers are ethically sourced. We work closely with local growers and suppliers to ensure that our flowers are both beautiful and eco-friendly.</p>
</div>
<div class="abs flower-card" style="left:782px">
  <div class="photo" style="background:radial-gradient(circle at 50% 50%,#8c86d8,#5a5a9e 25%,#3c5a30 55%,#2a2a2a)" role="img" aria-label="Photo of purple fan flower in a pot"></div>
  <p>We believe that sustainability is important, and as such, all of our native flowers are ethically sourced. We work closely with local growers and suppliers to ensure that our flowers are both beautiful and eco-friendly.</p>
</div>
<a class="abs btn" style="left:518px;top:2113px" href="#">READ MORE</a>

<section class="abs gift-text">
  <h2 class="section-title">Giftwear</h2>
  <p>We are proud to offer a wide range of unique and high-quality gifts that celebrate the natural beauty of Australia's native flora and fauna. From beautifully scented candles to stunning artworks, our gift selection is sure to please.</p>
  <p>Our giftware collection features a range of products that have been designed and crafted by local artisans and small businesses. We believe in supporting our community and showcasing the amazing talent and creativity that can be found here in Australia.</p>
  <p>In addition to our locally made products, we also stock gifts from well-known brands that share our passion for nature and sustainability.</p>
  <a class="btn" href="#" style="margin-top:4px">READ MORE</a>
</section>
<div class="abs gift-big" role="img" aria-label="Photo of a native flower bouquet with gum blossom"></div>
<div class="abs gift-small" role="img" aria-label="Photo of native flowers and foliage"></div>

<div class="abs history-band"></div>
<div class="abs deco" style="left:0;top:3110px;width:170px;height:170px" role="img" aria-label="Faint line drawing of flannel flowers"></div>
<div class="abs history-head"><h2 class="section-title">History</h2></div>
<p class="abs history-intro">The Bramble Hollow business, that has been providing plants, flowers and native giftware to the Fernvale Ranges and surrounding areas since 1996. Over this time, we have established a strong connection with the community and provided expert native advice.</p>
<div class="abs video" role="img" aria-label="Video of flannel flowers growing on coastal dunes by the sea"></div>
<div class="abs play"><svg width="68" height="68" viewBox="0 0 68 68" aria-hidden="true"><path d="M27 20 L27 48 L49 34Z" fill="#fff"/></svg></div>

<div class="abs now-head"><h2>The nursery now</h2></div>
<div class="abs deco" style="left:850px;top:3630px;width:280px;height:280px" role="img" aria-label="Faint line drawing of flannel flowers"></div>
<h2 class="abs now-title">Since then concentrating strictly on native only</h2>
<div class="abs now-text">
  <p>The business was originally established by Maren and Tessaly, ** later departed and Corinne and Idalie.</p>
  <p>Maren Holt has been in the native plant industry for most of her life. She has been involved in the propagation, wholesale, retail, floral design and promotion of native plants.</p>
</div>
<div class="abs now-photo" role="img" aria-label="Photo of white native flower clusters among green foliage"></div>

<svg class="abs footer-wave" viewBox="0 0 1200 600" preserveAspectRatio="none" aria-hidden="true">
  <path d="M0 0 C200 90 430 120 640 110 C880 95 1060 70 1200 20 L1200 600 L0 600Z" fill="#0f7b63"/>
</svg>
<footer>
  <a class="abs footer-brand" href="#">The<br>Bramble<br>Hollow</a>
  <div class="abs footer-col links" style="left:396px;top:4420px">
    <h3>Links</h3>
    <ul><li>Home</li><li>Nursery</li><li>Native flowers</li><li>Giftwear</li><li>About</li></ul>
  </div>
  <div class="abs footer-col" style="left:554px;top:4420px;width:220px">
    <h3 style="margin-left:8px">Contact Us</h3>
    <div class="contact-row"><span class="contact-ico"><svg width="16" height="18" viewBox="0 0 24 24" aria-hidden="true"><path fill="#fff" d="M12 2a7 7 0 0 0-7 7c0 5 7 13 7 13s7-8 7-13a7 7 0 0 0-7-7zm0 9.5A2.5 2.5 0 1 1 12 6.5a2.5 2.5 0 0 1 0 5z"/></svg></span><span>Location Name<br>Dummy address livv<br>Australia</span></div>
    <div class="contact-row" style="align-items:center"><span class="contact-ico"><svg width="16" height="16" viewBox="0 0 24 24" aria-hidden="true"><path fill="#fff" d="M6.6 10.8a15 15 0 0 0 6.6 6.6l2.2-2.2c.3-.3.7-.4 1-.2 1.1.4 2.3.6 3.6.6.6 0 1 .4 1 1V20c0 .6-.4 1-1 1A17 17 0 0 1 3 4c0-.6.4-1 1-1h3.5c.6 0 1 .4 1 1 0 1.3.2 2.5.6 3.6.1.3 0 .7-.2 1z"/></svg></span><span>Phone:402.118.5530</span></div>
    <div class="contact-row" style="align-items:center"><span class="contact-ico"><svg width="16" height="14" viewBox="0 0 24 20" aria-hidden="true"><path fill="#fff" d="M2 2h20v16H2zm2 2v.5l8 5 8-5V4zm0 3v9h16V7l-8 5z"/></svg></span><span>hello@bramblehollow.example</span></div>
  </div>
  <div class="abs footer-col" style="left:828px;top:4420px;width:270px">
    <h3>Newsletter Sign up</h3>
    <p style="margin-top:-6px">Lorem ipsum dolor sit amelor &nbsp;conse ctet ur adipisclorem ipsumlit,</p>
    <div class="email"><span>Email</span><span class="email-go"><svg width="22" height="14" viewBox="0 0 22 14" aria-hidden="true"><path d="M1 7h19M14 1l6 6-6 6" stroke="#fff" stroke-width="2" fill="none"/></svg></span></div>
    <div class="social-foot">
      <a href="#" aria-label="Social link one"></a>
      <a href="#" aria-label="Social link two"></a>
      <a href="#" aria-label="Social link three"></a>
      <a href="#" aria-label="Social link four"></a>
    </div>
  </div>
  <div class="abs footer-rule"></div>
  <p class="abs copyright">© 2023 All Rights Reserved.Terms &amp; Conditions Privacy Policy</p>
</footer>

</body>
</html>
```